Business Card Design Project

parking lot sealing and striping company

Industry/Entity Type

Business

Contact Information for Business Card

See pics below, blue and gray colors

```html
<!DOCTYPE html>
<html lang="en">
<head>
<meta charset="utf-8">
<title>Prairie Line Paving – Business Card</title>
<link href="https://fonts.googleapis.com/css2?family=Open+Sans:wght@400;600;700&family=Rubik:wght@700&display=swap" rel="stylesheet">
<style>
  :root {
    --asphalt-dark: #0b0b0c;
    --asphalt-mid: #1c1c1e;
    --asphalt-light: #2a2a2c;
    --brand-blue: #2f52ad;
    --icon-blue: #3557b8;
    --silver: #d6d6d8;
    --silver-dim: #a9a9ab;
    --contact-gray: #c9c9cb;
    --service-gray: #bcbcbe;
  }
  html, body {
    margin: 0;
    padding: 0;
    width: 1200px;
    height: 720px;
    overflow: hidden;
    background: var(--asphalt-dark);
  }
  .card {
    position: relative;
    width: 1200px;
    height: 720px;
    overflow: hidden;
    font-family: "Open Sans", Arial, sans-serif;
    background:
      radial-gradient(ellipse 70% 55% at 45% 30%, var(--asphalt-light) 0%, var(--asphalt-mid) 45%, var(--asphalt-dark) 100%);
  }
  .brand-name {
    position: absolute;
    left: 80px;
    top: 178px;
    margin: 0;
    font-family: "Rubik", Arial, sans-serif;
    font-weight: 700;
    font-size: 76px;
    line-height: 1;
    letter-spacing: 1px;
    color: var(--silver);
    white-space: nowrap;
  }
  .worker-illustration {
    position: absolute;
    left: 818px;
    top: 70px;
    width: 296px;
    height: 202px;
    border-radius: 6px;
    background: linear-gradient(180deg, #e6e6e8 0%, #a8a8aa 100%);
    opacity: 0.85;
  }
  .divider {
    position: absolute;
    left: 0;
    top: 370px;
    width: 1200px;
    height: 6px;
    background: linear-gradient(180deg, #f2f2f2 0%, #9a9a9c 100%);
  }
  .owner-name {
    position: absolute;
    left: 80px;
    top: 398px;
    margin: 0;
    font-weight: 700;
    font-size: 30px;
    letter-spacing: 0.5px;
    color: var(--brand-blue);
  }
  .contact-list {
    position: absolute;
    left: 80px;
    top: 470px;
    margin: 0;
    padding: 0;
    list-style: none;
  }
  .contact-item {
    display: flex;
    align-items: center;
    height: 44.5px;
    font-weight: 700;
    font-size: 29px;
    color: var(--contact-gray);
  }
  .contact-icon {
    width: 34px;
    height: 34px;
    margin-right: 16px;
    flex: none;
  }
  .service-column {
    position: absolute;
    top: 396px;
    margin: 0;
    padding: 0;
    list-style: none;
  }
  .service-column.left { left: 518px; }
  .service-column.right { left: 822px; }
  .service-item {
    position: relative;
    height: 45px;
    padding-left: 27px;
    font-size: 21px;
    line-height: 45px;
    color: var(--service-gray);
    white-space: nowrap;
  }
  .service-item::before {
    content: "";
    position: absolute;
    left: 0;
    top: 18px;
    width: 9px;
    height: 9px;
    border-radius: 50%;
    background: var(--icon-blue);
  }
</style>
</head>
<body>
<main class="card">
  <h1 class="brand-name">Prairie Line Paving</h1>
  <div class="worker-illustration" role="img" aria-label="Silver silhouette of a worker pushing a line-striping machine"></div>

  <div class="divider"></div>

  <h2 class="owner-name">DANIEL HARKER</h2>

  <ul class="contact-list">
    <li class="contact-item">
      <svg class="contact-icon" viewBox="0 0 34 34" aria-hidden="true">
        <rect x="9" y="2" width="16" height="30" rx="3" fill="none" stroke="var(--icon-blue)" stroke-width="3"/>
        <circle cx="17" cy="27" r="1.8" fill="var(--icon-blue)"/>
      </svg>
      (555) 214-0175
    </li>
    <li class="contact-item">
      <svg class="contact-icon" viewBox="0 0 34 34" aria-hidden="true">
        <path d="M7 3 L13 3 L15 11 L11 14 Q14 21 20 24 L23 20 L31 22 L31 28 Q31 31 27 31 Q13 29 5 15 Q3 9 3 6 Q3 3 7 3 Z" fill="var(--icon-blue)"/>
      </svg>
      (555) 516-0192
    </li>
    <li class="contact-item">
      <svg class="contact-icon" viewBox="0 0 34 34" aria-hidden="true">
        <g fill="none" stroke="var(--icon-blue)" stroke-width="2.4">
          <circle cx="17" cy="17" r="14"/>
          <ellipse cx="17" cy="17" rx="6" ry="14"/>
          <line x1="3" y1="17" x2="31" y2="17"/>
          <path d="M6 9 H28 M6 25 H28"/>
        </g>
      </svg>
      www.prairielinepav.com
    </li>
    <li class="contact-item">
      <svg class="contact-icon" viewBox="0 0 34 34" aria-hidden="true">
        <rect x="2" y="7" width="30" height="21" rx="2" fill="var(--icon-blue)"/>
        <path d="M3 9 L17 20 L31 9" fill="none" stroke="#0d0d0e" stroke-width="2.4"/>
      </svg>
      prairielinepav@mail.com
    </li>
  </ul>

  <ul class="service-column left">
    <li class="service-item"></li>
    <li class="service-item"></li>
    <li class="service-item">SEALCOATING</li>
    <li class="service-item">RE STRIPING</li>
    <li class="service-item">ASPHALT REPAIR</li>
    <li class="service-item">CONCRETE REPAIR</li>
  </ul>

  <ul class="service-column right">
    <li class="service-item"></li>
    <li class="service-item"></li>
    <li class="service-item">CRACK FILLING</li>
    <li class="service-item">ADA COMPLIANCIANT</li>
    <li class="service-item">PARKING LOT LAY OUT</li>
    <li class="service-item">ASPHALT PATCHING</li>
  </ul>
</main>
</body>
</html>
```